Pipelining Product Supply Company Needs New Stationery

We need new stationery (letter head, with compliments slips & business card) for our industry leading pipe lining supply company. basically we sell product to other plumbers to carry out pipe relining.

Im looking for something, fresh, professional, sleek and modern at the same time.

Ive attached a copy of the logo and also some guidelines to follow for colours and fonts etc.

Target Market(s)

Plumbers

Industry/Entity Type

Plumbing

Font styles to use
Sans Serif

Requirements
Must have
• The logo, space for ABN, Address, Phone Number, website and email.
Nice to have
• Stand out from the crowd. To look sleep and professional.
Should not have
• Any other colours apart from what is on the guidelines.

```html
<!DOCTYPE html>
<html lang="en">
<head>
<meta charset="utf-8">
<title>Harbourline Reline Supplies – Business Card</title>
<link href="https://fonts.googleapis.com/css2?family=Open+Sans:wght@400;600;700&display=swap" rel="stylesheet">
<style>
  :root {
    --bg: #3a3a3c;
    --green-deep: #1f5e10;
    --green-mid: #3f8f1e;
    --green-light: #7fd13a;
    --green-text: #6cc22d;
    --grey-text: #6e6e6e;
    --grey-line: #a9a9a9;
    --paper: #f7f7f5;
    --white: #ffffff;
  }
  * { box-sizing: border-box; margin: 0; padding: 0; }
  html, body { width: 1200px; height: 960px; overflow: hidden; }
  body {
    background: var(--bg);
    font-family: "Open Sans", Arial, sans-serif;
    position: relative;
  }
  .card {
    position: absolute;
    left: 250px;
    width: 700px;
    height: 400px;
    overflow: hidden;
  }
  /* Back of card */
  .card-back {
    top: 50px;
    background: radial-gradient(ellipse at 45% 45%, var(--green-light) 0%, var(--green-mid) 40%, var(--green-deep) 100%);
    display: flex;
    flex-direction: column;
    align-items: center;
    justify-content: center;
    gap: 34px;
  }
  .back-brand {
    display: flex;
    align-items: center;
    gap: 16px;
    color: var(--white);
    font-size: 40px;
    font-weight: 600;
    letter-spacing: 1px;
  }
  .brand-dot {
    width: 22px; height: 22px; border-radius: 50%;
    background: var(--white);
    flex: none;
  }
  .back-web {
    color: var(--white);
    font-size: 20px;
    letter-spacing: 0.5px;
  }
  /* Front of card */
  .card-front {
    top: 500px;
    background: var(--paper);
    border-bottom: 12px solid var(--green-mid);
  }
  .front-brand {
    position: absolute;
    right: 40px;
    top: 70px;
    display: flex;
    align-items: center;
    gap: 12px;
    color: var(--green-mid);
    font-size: 28px;
    font-weight: 600;
  }
  .front-brand .brand-dot { background: var(--green-mid); width: 16px; height: 16px; }
  .person { position: absolute; left: 40px; top: 122px; }
  .person-name {
    color: var(--green-text);
    font-size: 24px;
    font-weight: 700;
    text-transform: uppercase;
    line-height: 1.1;
  }
  .person-role {
    color: var(--grey-text);
    font-size: 17px;
    text-transform: uppercase;
    margin-top: 2px;
  }
  .divider {
    position: absolute;
    left: 40px; right: 40px;
    top: 205px;
    height: 1px;
    background: var(--grey-line);
  }
  .contacts {
    position: absolute; left: 40px; top: 222px;
    list-style: none;
    color: var(--grey-text);
    font-size: 18px;
    line-height: 30px;
  }
  .contacts li { display: flex; align-items: center; gap: 12px; }
  .contacts svg { width: 16px; height: 16px; fill: var(--green-mid); flex: none; }
  .address {
    position: absolute; right: 40px; bottom: 34px;
    text-align: right;
    color: var(--grey-text);
    font-size: 18px;
    font-weight: 600;
    font-style: normal;
    line-height: 28px;
  }
</style>
</head>
<body>
  <section class="card card-back" aria-label="Card back">
    <div class="back-brand"><span class="brand-dot"></span>Harbourline Reline Supplies</div>
    <div class="back-web">harbourlinerelinesupplies.com</div>
  </section>

  <section class="card card-front" aria-label="Card front">
    <div class="front-brand"><span class="brand-dot"></span>Harbourline Reline Supplies</div>
    <div class="person">
      <div class="person-name">Tamsin Varloe</div>
      <div class="person-role">President</div>
    </div>
    <div class="divider"></div>
    <ul class="contacts">
      <li>
        <svg viewBox="0 0 16 16" aria-hidden="true"><path d="M3 1h3l1.5 4-2 1.2a9 9 0 0 0 4.3 4.3L11 8.5l4 1.5v3a2 2 0 0 1-2 2A12 12 0 0 1 1 3a2 2 0 0 1 2-2z"/></svg>
        555 0142 7780
      </li>
      <li>
        <svg viewBox="0 0 16 16" aria-hidden="true"><path d="M1 3h14v10H1z M1 3l7 6 7-6"/></svg>
        info@hrlsupply-co.com
      </li>
      <li>
        <svg viewBox="0 0 16 16" aria-hidden="true"><circle cx="8" cy="8" r="7"/></svg>
        www.hrlsupply-co.com
      </li>
    </ul>
    <address class="address">
      27 Quellbrook Row<br>
      Dunmarsh, NY 11099<br>
      ABN: 4081223659
    </address>
  </section>
</body>
</html>
```